Vellmar Concrete

We are looking for a design for a two sided over-sized postcard to show the beauty of the work we provide. We want it to be simple, bold & elegant as well as eye catching. Feel free to crop the images supplied to whatever looks best.

Website is www.vkq-lonestarpour.com for more information, verbiage, contact information, etc.

Industry/Entity Type

Concrete

```html
<!DOCTYPE html>
<html lang="en">
<head>
<meta charset="utf-8">
<title>Vellmar Concrete – Postcard</title>
<link rel="stylesheet" href="https://fonts.googleapis.com/css2?family=Francois+One&family=Roboto+Condensed:wght@400;700&family=Ropa+Sans&display=swap">
<style>
  :root {
    --page-bg: #eeeeee;
    --brown: #5a4a42;
    --brown-dark: #4a3c35;
    --grey-light: #b9b9b9;
    --grey-mid: #9a9a9a;
    --grey-logo: #8c8c8c;
    --green: #8cc63f;
    --white: #ffffff;
    --tan: #d9c3a6;
  }
  * { margin: 0; padding: 0; box-sizing: border-box; }
  html, body { width: 1200px; height: 900px; overflow: hidden; background: var(--page-bg); }
  .postcard {
    position: absolute; left: 138px; top: 93px; width: 945px; height: 607px;
    background: var(--brown);
    box-shadow: 0 4px 10px rgba(0,0,0,.35);
    overflow: hidden;
  }
  .side-panel {
    position: absolute; left: 0; top: 0; width: 279px; height: 100%;
    background: linear-gradient(100deg, var(--grey-mid) 0%, var(--grey-light) 40%, #a8a8a8 70%, #c4c4c4 100%);
    border-right: 2px solid #d0d0d0;
  }
  .logo-band {
    position: absolute; left: 0; top: 75px; width: 40px; height: 92px; background: var(--brown);
  }
  .logo-box {
    position: absolute; left: 38px; top: 75px; width: 308px; height: 92px;
    background: var(--grey-logo);
    border: 3px solid #a5a5a5;
    display: flex; align-items: center; gap: 14px; padding-left: 22px;
  }
  .logo-mark { width: 50px; height: 56px; background: var(--brown); flex: none; }
  .logo-name {
    font-family: "Francois One", sans-serif; font-size: 30px; line-height: 1;
    color: var(--brown); text-transform: uppercase; letter-spacing: .5px;
  }
  .estimate {
    position: absolute; left: 38px; top: 194px;
    font-family: "Francois One", sans-serif; font-size: 22px; color: var(--white);
    letter-spacing: .3px; white-space: nowrap;
    text-shadow: 0 1px 2px rgba(0,0,0,.4);
  }
  .accent { position: absolute; }
  .accent-top { left: 32px; top: 265px; }
  .accent-bottom { left: 234px; top: 412px; }
  .services {
    position: absolute; left: 52px; top: 286px; width: 195px;
    font-family: "Roboto Condensed", sans-serif; font-weight: 700;
    font-size: 15.5px; line-height: 22.5px; color: var(--brown);
    text-align: justify;
  }
  .contact { position: absolute; left: 0; top: 490px; width: 279px; text-align: center; }
  .call-now {
    font-family: "Roboto Condensed", sans-serif; font-weight: 700; font-size: 20px;
    color: var(--white); line-height: 1;
  }
  .phone {
    font-family: "Roboto Condensed", sans-serif; font-weight: 700; font-size: 35px;
    color: var(--brown); line-height: 1.05; letter-spacing: .5px;
    -webkit-text-stroke: 1px var(--white);
  }
  .website {
    font-family: "Roboto Condensed", sans-serif; font-weight: 700; font-size: 12.5px;
    color: var(--white); letter-spacing: 1.5px; margin-top: 2px;
  }
  .tagline {
    position: absolute; left: 279px; right: 0; top: 34px; text-align: center;
    font-family: "Ropa Sans", sans-serif; font-size: 17px; color: var(--tan);
  }
  .project-photo {
    position: absolute; box-shadow: 3px 4px 7px rgba(0,0,0,.5);
  }
  .photo-stamped-floor { left: 402px; top: 77px; width: 232px; height: 153px; background: linear-gradient(135deg, #6b5340, #a68a63 55%, #5e4a38); }
  .photo-garden { left: 663px; top: 77px; width: 233px; height: 153px; background: linear-gradient(180deg, #7a9a5a, #a0623e 50%, #5c8a3e); }
  .photo-patio { left: 324px; top: 246px; width: 234px; height: 154px; background: linear-gradient(120deg, #9a6a50, #b07a5c 45%, #5f8a3a); }
  .photo-slate { left: 586px; top: 246px; width: 233px; height: 154px; background: linear-gradient(120deg, #7a8a78, #9a8a60 55%, #6a2a3a); }
  .photo-garage { left: 402px; top: 415px; width: 232px; height: 155px; background: linear-gradient(180deg, #5a5a5a, #9a948a 40%, #b0a898); }
  .photo-pavers { left: 663px; top: 415px; width: 233px; height: 155px; background: linear-gradient(90deg, #8a3a28, #b0683c 50%, #c9a77c); }
</style>
</head>
<body>
  <section class="postcard">
    <aside class="side-panel">
      <div class="logo-band"></div>
      <div class="logo-box">
        <span class="logo-mark"></span>
        <span class="logo-name">Vellmar<br>Concrete</span>
      </div>
      <p class="estimate">Always a FREE ESTIMATE!</p>
      <svg class="accent accent-top" width="24" height="54" viewBox="0 0 24 54"><polygon points="0,0 24,0 6,54" fill="var(--green)"/></svg>
      <p class="services">We are able to offer very basic color concepts to full depth, multi-layer works of art and will assist you in the process to select what would look best based on your personal preferences.</p>
      <svg class="accent accent-bottom" width="24" height="56" viewBox="0 0 24 56"><polygon points="24,0 24,56 0,56" fill="var(--green)"/></svg>
      <div class="contact">
        <p class="call-now">CALL NOW!</p>
        <p class="phone">832-555-0147</p>
        <p class="website">www.vkq-lonestarpour.com</p>
      </div>
    </aside>
    <p class="tagline">Call or email us and let’s discuss how we can bring beauty to your space.</p>
    <div class="project-photo photo-stamped-floor" role="img" aria-label="Stamped decorative concrete floor with curved bands"></div>
    <div class="project-photo photo-garden" role="img" aria-label="Backyard garden with wooden fence and flower beds"></div>
    <div class="project-photo photo-patio" role="img" aria-label="Curved stamped concrete patio beside a lawn"></div>
    <div class="project-photo photo-slate" role="img" aria-label="Slate-look stamped walkway next to a red maple shrub"></div>
    <div class="project-photo photo-garage" role="img" aria-label="Exposed aggregate garage floor with a parked car"></div>
    <div class="project-photo photo-pavers" role="img" aria-label="Hexagonal paver-pattern concrete in red and tan tones"></div>
  </section>
</body>
</html>
```